Looking for a creative label design for our retail coffee bags

We are a coffee manufacturer (coffee roaster) looking to re-brand our retail label for our coffee bags. Our main coffee blend that we sell is our Harborline Velvet Blend. You can use this name when creating the label. We are going for a look that represents our company as a coffee roaster. Please reference our website (www.brindlemugworks.com) and our Facebook page to learn more about our company and to give you more inspiration on creating this design.

Target Market(s)

Retail customers/grocery stores

Industry/Entity Type

Manufacturer

Requirements
Must have
• The size of the label has to be 3" width x 4" height

Logo must be Black
Nice to have
• We currently incorporate a color on our labels for each blend. For example, Harborline Velvet Blend (royal blue), Decaffeinated Blend (red), Breakfast Blend (green), Flavored coffees (gold).

Rustic/vintage style

```html
<!DOCTYPE html>
<html lang="en">
<head>
<meta charset="utf-8">
<title>Brindle Mugworks – Retail Coffee Labels</title>
<link rel="stylesheet" href="https://fonts.googleapis.com/css2?family=Roboto:wght@400;500;700&family=Dancing+Script:wght@500&display=swap">
<style>
  :root {
    --paper: #ffffff;
    --canvas: #ffffff;
    --green: #5c6b3a;
    --charcoal: #2e2e2e;
    --blue: #0d5aa7;
    --red: #bd1a1f;
  }
  * { box-sizing: border-box; margin: 0; padding: 0; }
  html, body { width: 1200px; height: 1200px; overflow: hidden; background: var(--canvas); }
  .canvas { position: relative; width: 1200px; height: 1200px; }

  .label {
    position: absolute;
    width: 337px;
    height: 449px;
    background: var(--paper);
    color: var(--accent);
    box-shadow: 0 4px 10px rgba(0,0,0,0.25);
    overflow: hidden;
  }
  .label--breakfast { left: 36px; top: 87px; --accent: var(--green); }
  .label--flavored { left: 836px; top: 91px; --accent: var(--charcoal); }
  .label--harborline { left: 36px; top: 589px; --accent: var(--blue); }
  .label--decaf { left: 829px; top: 581px; --accent: var(--red); }
  .label--featured { left: 431px; top: 375px; --accent: var(--blue); }

  .label__frame {
    position: absolute;
    left: 12px; right: 12px; top: 16px; bottom: 26px;
    border: 1px solid var(--accent);
  }
  .label__tab {
    position: absolute;
    left: 128px; top: 0;
    width: 81px; height: 80px;
    background: var(--accent);
  }
  .label__seal {
    position: absolute;
    left: 110px; top: 68px;
    width: 117px; height: 117px;
    border-radius: 50%;
    background: var(--accent);
    display: flex; flex-direction: column;
    align-items: center; justify-content: center;
  }
  .label__brand {
    font-family: "Roboto", sans-serif;
    font-weight: 500;
    font-size: 14px;
    letter-spacing: 1.5px;
    line-height: 1.25;
    color: var(--paper);
    text-align: center;
  }
  .label__title {
    position: absolute;
    left: 0; right: 0; top: 222px;
    text-align: center;
    font-family: "Roboto", sans-serif;
    font-weight: 500;
    font-size: 27px;
    letter-spacing: 0.3px;
    line-height: 1;
  }
  .label__subtitle {
    position: absolute;
    left: 0; right: 0; top: 254px;
    text-align: center;
    font-family: "Roboto", sans-serif;
    font-weight: 400;
    font-size: 14px;
    line-height: 1;
  }
  .label__roaster {
    position: absolute;
    left: 0; right: 0; top: 268px;
    text-align: center;
    font-family: "Dancing Script", cursive;
    font-weight: 500;
    font-size: 25px;
    line-height: 1;
  }
  .label--flavored .label__roaster { top: 258px; }
  .label__botanical {
    position: absolute;
    left: 118px; top: 302px;
    width: 100px; height: 84px;
    border-radius: 40% 50% 45% 55%;
    background: radial-gradient(circle at 50% 50%, color-mix(in srgb, var(--accent) 22%, white), color-mix(in srgb, var(--accent) 6%, white) 70%, transparent 72%);
  }
  .label__band {
    position: absolute;
    left: 0; right: 0; bottom: 0;
    height: 27px;
    background: var(--accent);
  }
  .label__weight {
    position: absolute;
    left: 104px; bottom: 14px;
    width: 129px; height: 30px;
    border-radius: 15px 15px 0 0;
    background: var(--accent);
    color: var(--paper);
    font-family: "Roboto", sans-serif;
    font-weight: 700;
    font-size: 14px;
    display: flex; align-items: center; justify-content: center;
    padding-top: 2px;
  }
</style>
</head>
<body>
<main class="canvas">

  <article class="label label--breakfast">
    <div class="label__frame"></div>
    <div class="label__tab"></div>
    <div class="label__seal"><span class="label__brand">BRINDLE<br>MUGWORKS</span></div>
    <h2 class="label__title">BREAKFAST BLEND</h2>
    <p class="label__subtitle">SUPREMO BLEND</p>
    <p class="label__roaster" style="top:272px">Coffee Roaster</p>
    <div class="label__botanical" role="img" aria-label="Line drawing of a coffee branch with blossoms and cherries"></div>
    <div class="label__band"></div>
    <div class="label__weight">Nt. Wt:16 oz</div>
  </article>

  <article class="label label--flavored">
    <div class="label__frame"></div>
    <div class="label__tab"></div>
    <div class="label__seal"><span class="label__brand">BRINDLE<br>MUGWORKS</span></div>
    <h2 class="label__title">FLAVORED COFFEES</h2>
    <p class="label__roaster">Coffee Roaster</p>
    <div class="label__botanical" role="img" aria-label="Line drawing of a coffee branch with blossoms and cherries"></div>
    <div class="label__band"></div>
    <div class="label__weight">Nt. Wt:16 oz</div>
  </article>

  <article class="label label--featured">
    <div class="label__frame"></div>
    <div class="label__tab"></div>
    <div class="label__seal"><span class="label__brand">BRINDLE<br>MUGWORKS</span></div>
    <h2 class="label__title">HARBORLINE</h2>
    <p class="label__subtitle">VELVET BLEND</p>
    <p class="label__roaster" style="top:272px">Coffee Roaster</p>
    <div class="label__botanical" role="img" aria-label="Line drawing of a coffee branch with blossoms and cherries"></div>
    <div class="label__band"></div>
    <div class="label__weight">Nt. Wt:16 oz</div>
  </article>

  <article class="label label--harborline">
    <div class="label__frame"></div>
    <div class="label__tab"></div>
    <div class="label__seal"><span class="label__brand">BRINDLE<br>MUGWORKS</span></div>
    <h2 class="label__title">HARBORLINE</h2>
    <p class="label__subtitle">VELVET BLEND</p>
    <p class="label__roaster" style="top:272px">Coffee Roaster</p>
    <div class="label__botanical" role="img" aria-label="Line drawing of a coffee branch with blossoms and cherries"></div>
    <div class="label__band"></div>
    <div class="label__weight">Nt. Wt:16 oz</div>
  </article>

  <article class="label label--decaf">
    <div class="label__frame"></div>
    <div class="label__tab"></div>
    <div class="label__seal"><span class="label__brand">BRINDLE<br>MUGWORKS</span></div>
    <h2 class="label__title">DECAFFEINATED</h2>
    <p class="label__subtitle">BLEND</p>
    <p class="label__roaster" style="top:272px">Coffee Roaster</p>
    <div class="label__botanical" role="img" aria-label="Line drawing of a coffee branch with blossoms and cherries"></div>
    <div class="label__band"></div>
    <div class="label__weight">Nt. Wt:16 oz</div>
  </article>

</main>
</body>
</html>
```